Etikettendesign für Imkereiprodukt
Zielgruppe
Ich betreibe eine Imkerei nach ökologischen Gesichtspunkten und vertreibe alles rund um die Biene- Honig, Wachs, Met, Likör...
Aus Bienenwachs und reinem Leinöl stelle ich ein natürliches Holzwachs her. (Wachs stammt aus eigener Bio Imkerei, Leinöl wird in Deutschland hergestellt)
Mit dem Wachs werden unbehandelte Hölzer imprägniert, gegen Feuchtigkeit geschützt, das Wachs verleiht dem Holz einen matten Glanz
Für dieses Produkt benötige ich ein Etikett.
Aufgabenstellung
- rundes Etikett Durchmesser 85 mm
- Verwendung von eigenem Firmenlogo (Anhang) (Name der Imkerei auch 'Wabenritter')
- Verwendung von folgenden Textbausteinen:
'ausschließlich Leinöl und Bienenwachs'
'regional von Hand hergestellt'
'komplett ohne Lösungsmittel'
oder ähnlich
- Herstelleradresse
- Datei nach Druck-vorgaben

```html
<!DOCTYPE html>
<html lang="de">
<head>
<meta charset="utf-8">
<title>Wabenritter – Holzwachs Etikett</title>
<link rel="stylesheet" href="https://fonts.googleapis.com/css2?family=Zilla+Slab:wght@600;700&family=Asap+Condensed:wght@400;500;600&display=swap">
<style>
  :root {
    --bg: #f4f4f4;
    --ink: #1b1b1b;
    --gold: #b39b5c;
    --grey: #6e6e6e;
    --paper: #ffffff;
  }
  html, body {
    margin: 0;
    padding: 0;
    width: 1200px;
    height: 1199px;
    overflow: hidden;
    background: var(--bg);
  }
  .canvas {
    position: relative;
    width: 1200px;
    height: 1199px;
  }
  .label {
    position: absolute;
    left: 320px;
    top: 319px;
    width: 560px;
    height: 560px;
  }
  .label-shape {
    position: absolute;
    inset: 0;
  }
  .label-content {
    position: absolute;
    inset: 0;
    text-align: center;
  }
  .brand-mark {
    position: absolute;
    left: 50%;
    top: 62px;
    width: 96px;
    height: 96px;
    margin-left: -48px;
    border-radius: 50%;
    background: var(--gold);
  }
  .brand-name {
    position: absolute;
    left: 0; right: 0;
    top: 184px;
    margin: 0;
    font-family: "Zilla Slab", serif;
    font-weight: 700;
    font-size: 25px;
    letter-spacing: 2.5px;
    color: var(--ink);
  }
  .tagline {
    position: absolute;
    left: 0; right: 0;
    top: 248px;
    margin: 0;
    font-family: "Zilla Slab", serif;
    font-weight: 700;
    font-size: 15px;
    letter-spacing: 1.6px;
    color: var(--ink);
  }
  .product-band {
    position: absolute;
    left: 127px;
    top: 279px;
    width: 306px;
    height: 46px;
  }
  .product-name {
    position: absolute;
    left: 0; right: 0;
    top: 284px;
    margin: 0;
    font-family: "Zilla Slab", serif;
    font-weight: 700;
    font-size: 25px;
    color: var(--ink);
  }
  .features {
    position: absolute;
    left: 0; right: 0;
    top: 340px;
    margin: 0;
    padding: 0;
    list-style: none;
    font-family: "Asap Condensed", sans-serif;
    font-size: 17px;
    line-height: 22px;
    color: var(--grey);
  }
  .features li::before { content: "· "; }
  .maker {
    position: absolute;
    left: 0; right: 0;
    top: 412px;
    margin: 0;
    font-family: "Asap Condensed", sans-serif;
    font-style: normal;
    font-weight: 600;
    font-size: 13.5px;
    line-height: 17px;
    color: var(--gold);
  }
</style>
</head>
<body>
<main class="canvas">
  <section class="label" aria-label="Rundes Etikett Holzwachs">
    <svg class="label-shape" viewBox="0 0 560 560" role="img" aria-label="Holzscheibe mit Jahresringen und Rinde als Etikettform">
      <circle cx="280" cy="280" r="272" fill="var(--ink)"/>
      <circle cx="280" cy="280" r="252" fill="var(--paper)"/>
      <circle cx="280" cy="280" r="238" fill="none" stroke="var(--ink)" stroke-width="1.5"/>
      <circle cx="280" cy="280" r="226" fill="none" stroke="var(--ink)" stroke-width="1"/>
    </svg>
    <div class="label-content">
      <span class="brand-mark" aria-hidden="true"></span>
      <h1 class="brand-name">WABENRITTER</h1>
      <p class="tagline">REGIONAL VON HAND HERGESTELLT</p>
      <svg class="product-band" viewBox="0 0 306 46" aria-hidden="true">
        <polygon points="4,3 302,0 298,44 0,46" fill="var(--gold)"/>
      </svg>
      <h2 class="product-name">Holzwachs</h2>
      <ul class="features">
        <li>ausschließlich Leinöl und Bienenwachs</li>
        <li>komplett ohne Lösungsmittel</li>
      </ul>
      <address class="maker">
        Imkerei Wabenhof<br>
        Lindenweg 4, 12345 Musterfeld<br>
        www.wabenritter-imkerei.de
      </address>
    </div>
  </section>
</main>
</body>
</html>
```